Cosmetic Clinic Looking For Sign Designs

We are looking for sign design ideas for the front of our building and a lawn sign for our cosmetic injection salon.
I have uploaded the front of our building for a mock up and size, lawn posts with size and a sign that uses the same dimensions.
We would like both signs to be black for the background.

Target Market(s)

Ages 18-75

Industry/Entity Type

Beauty

Requirements
Must have
• Services we offer:
• Cosmetic Injections
• Airbrush Spray Tanning
• Eyelash Growth Serum
• Skin Care Products & More
• Everything must be on a black background
• The lawn sign must have the address: 483 Fenwick and the building sign should have the phone number.
Should not have
• Nothing can light up (no LED)
• Both signs do not need the full address. Just 483 Fenwick and the phone number

```html
<!DOCTYPE html>
<html lang="en">
<head>
<meta charset="utf-8">
<title>Soft Bloom Studio — Signage</title>
<link rel="stylesheet" href="https://fonts.googleapis.com/css2?family=Open+Sans:wght@600;700;800&display=swap">
<style>
  :root {
    --sign-black: #0b0b0c;
    --brand-teal: #2a9fb8;
    --accent-pink: #e8207a;
    --ink-white: #ffffff;
    --backdrop: #e9e9ea;
  }
  * { box-sizing: border-box; margin: 0; padding: 0; }
  html, body { width: 1200px; height: 917px; overflow: hidden; }
  body {
    background: var(--backdrop);
    font-family: "Open Sans", Arial, sans-serif;
    position: relative;
  }

  /* ---------- Building fascia sign ---------- */
  .fascia-sign {
    position: absolute; left: 80px; top: 60px;
    width: 1040px; height: 235px;
    background: var(--sign-black);
  }
  .fascia-sign .brand {
    position: absolute; left: 40px; top: 0; width: 300px; height: 178px;
    display: flex; flex-direction: column; align-items: center; justify-content: center; gap: 12px;
  }
  .brand-dot {
    width: 58px; height: 58px; border-radius: 50%;
    border: 6px solid var(--accent-pink);
  }
  .brand-name {
    color: var(--brand-teal); font-weight: 800; letter-spacing: 1px;
    text-transform: uppercase; text-align: center; line-height: 1.1;
  }
  .fascia-sign .brand-name { font-size: 30px; }

  .service-list { list-style: none; color: var(--ink-white); font-weight: 700; text-transform: uppercase; text-align: center; }
  .service-list li::before {
    content: ""; display: inline-block; width: 8px; height: 8px; border-radius: 50%;
    background: var(--accent-pink); margin-right: 8px; vertical-align: middle; position: relative; top: -2px;
  }
  .fascia-sign .service-list {
    position: absolute; left: 420px; top: 18px; width: 520px;
    font-size: 24px; line-height: 36px;
  }

  .contact-band {
    position: absolute; left: 0; right: 0; bottom: 0;
    background: var(--brand-teal); border-top: 5px solid var(--accent-pink);
    color: var(--ink-white); font-weight: 700;
  }
  .fascia-sign .contact-band {
    height: 57px; display: flex; align-items: center; justify-content: space-around;
    font-size: 20px; padding: 0 40px;
  }
  .contact-item { display: flex; align-items: center; gap: 10px; }
  .contact-item svg { width: 24px; height: 24px; }
  .follow-dot { width: 20px; height: 20px; border-radius: 50%; background: var(--ink-white); }

  /* ---------- Lawn sign ---------- */
  .lawn-sign {
    position: absolute; left: 382px; top: 355px;
    width: 437px; height: 502px;
    background: var(--sign-black);
  }
  .lawn-sign .brand {
    position: absolute; left: 0; right: 0; top: 22px;
    display: flex; flex-direction: column; align-items: center; gap: 14px;
  }
  .lawn-sign .brand-dot { width: 70px; height: 70px; border-width: 7px; }
  .lawn-sign .brand-name { font-size: 30px; }
  .lawn-sign .service-list {
    position: absolute; left: 0; right: 0; top: 188px;
    font-size: 19px; line-height: 34px;
  }
  .lawn-sign .contact-band {
    height: 112px; text-align: center; padding-top: 14px;
  }
  .address { font-size: 26px; font-weight: 800; text-transform: uppercase; }
  .web { font-size: 17px; margin-top: 6px; }
</style>
</head>
<body>

  <section class="fascia-sign" aria-label="Building sign">
    <div class="brand">
      <div class="brand-dot"></div>
      <div class="brand-name">Soft Bloom<br>Studio</div>
    </div>
    <ul class="service-list">
      <li>Cosmetic Injections</li>
      <li>Airbrush Spray Tanning</li>
      <li>Eyelash Growth Serum</li>
      <li>Skin Care Products &amp; More</li>
    </ul>
    <div class="contact-band">
      <span class="contact-item">
        <svg viewBox="0 0 24 24" aria-hidden="true"><circle cx="12" cy="12" r="12" fill="#fff"/><path d="M8.5 6.5l2 2-1.2 1.6a7 7 0 0 0 4.6 4.6l1.6-1.2 2 2-1.5 1.7C11.5 17.5 6.5 12.5 6.8 8z" fill="#2a9fb8"/></svg>
        1 (555) 014 2270
      </span>
      <span class="contact-item">
        <svg viewBox="0 0 24 24" aria-hidden="true"><circle cx="12" cy="12" r="12" fill="#fff"/><g fill="none" stroke="#2a9fb8" stroke-width="1.6"><circle cx="12" cy="12" r="6.5"/><ellipse cx="12" cy="12" rx="2.8" ry="6.5"/><path d="M5.5 12h13"/></g></svg>
        www.softbloomstudio.com
      </span>
      <span class="contact-item">Follow Us <span class="follow-dot"></span></span>
    </div>
  </section>

  <section class="lawn-sign" aria-label="Lawn sign">
    <div class="brand">
      <div class="brand-dot"></div>
      <div class="brand-name">Soft Bloom<br>Studio</div>
    </div>
    <ul class="service-list">
      <li>Cosmetic Injections</li>
      <li>Airbrush Spray Tanning</li>
      <li>Eyelash Growth Serum</li>
      <li>Skin Care Products &amp; More</li>
    </ul>
    <div class="contact-band">
      <div class="address">483 Fenwick Street</div>
      <div class="web">www.softbloomstudio.com</div>
    </div>
  </section>

</body>
</html>
```